Poster for a 100 y.o. Tennis Tournament

I would like a poster designed to promote our tennis tournament but I'd like to avoid some of the clichés like the shadow of a player serving. Just well styled text would be fine but some clever imagery would be a bonus.
Highlighting the fact our tournament has been running for over 100 years would be nice so a retro design would work. But that doesn't mean a modern design, for example a minimalist approach utilising the lines of a tennis court, wouldn't work.
Updates

Our tennis committee is now in the process of short listing and will provide an update within 48 hours.

Industry/Entity Type

Court

Requirements
Must have
• The poster must contain the following text at a minimum:
"Brimley Tennis Tournament"/"Since 1908"
"9 March - 11 March, 2013" or "9-11 March, 2013", etc
"www.brimleytennis.com.au"

The poster must be reproducible in colour and black & white, or at least have an alternate for black & white.

The poster must be usable in both A3 and A4 sizes.
Nice to have
• The poster should contain the following text:
"Championship"
"Handicap"
"Seniors"
"Juniors"
Each above may be optionally succeeded by "Singles & Doubles", e.g. "Championship Singles & Doubles". It would actually be clearer if this additional text was used but would be repetitive, so alternate text "Singles & Doubles in all categories" might also be used. Alternatives for variety (with the first word the focus): "Championship Singles & Doubles", "Handicap Singles & Doubles", "Seniors 35+ & 50+", "Juniors 18&U, 14&U"

Ideally the poster will provision room for four to eight sponsors logos, preferably at the bottom, but failure to do this is not a show stopper.

The following text may also be used:
"Entries close February 24"
"Marnock Plate Weekend"

Attached is a photo of one of the old trophies. Utilisation of the curved style of the "Brimley Tennis Tournament" text would fit in with the history if the tournament.

The ability to reuse elements of the poster in a single page website used to promote the tournament would be an advantage (as it will provide consistency).

If you could have an image of a tennis ball that conveys the same energy as the clock/tyre image in the attached "Beyond the Hourglass" poster, that would be cool. Or using split imagery of a wooden racquet and a modern racquet, but with some energy, would also be good. These are just ideas though and by no means essential.

I've also attached a photo of a t-shirt with a poster layout I thought looked good.

Some additional text that can be used:
"Brand new courts"
"Corbin Field, Loxley Tce, Brimley"
"Phone 0427 318 642"
"Prizes and Trophies"

```html
<!DOCTYPE html>
<html lang="en">
<head>
<meta charset="utf-8">
<title>Brimley Tennis Tournament</title>
<link rel="stylesheet" href="https://fonts.googleapis.com/css2?family=Alfa+Slab+One&family=Archivo+Black&family=Bebas+Neue&family=Oswald:wght@400;500;600&family=Roboto+Condensed:ital,wght@1,800&family=Roboto+Slab:wght@800&display=swap">
<style>
  :root {
    --paper: #efe6d5;
    --paper-edge: #d9ccb5;
    --ink: #272421;
  }
  html, body {
    margin: 0;
    padding: 0;
    overflow: hidden;
    background: var(--paper);
  }
  .poster {
    display: block;
    width: 849px;
    height: 1200px;
  }
  .poster text { fill: var(--ink); }
  .title { font-family: "Bebas Neue", "Oswald", sans-serif; }
  .since { font-family: "Alfa Slab One", serif; }
  .intro { font-family: "Oswald", sans-serif; font-weight: 400; }
  .cat-championship { font-family: "Oswald", sans-serif; font-weight: 600; }
  .cat-seniors { font-family: "Roboto Slab", serif; font-weight: 800; }
  .cat-handicap { font-family: "Alfa Slab One", serif; }
  .cat-juniors { font-family: "Archivo Black", sans-serif; }
  .entries { font-family: "Oswald", sans-serif; font-weight: 500; }
  .dates { font-family: "Alfa Slab One", serif; }
  .web { font-family: "Roboto Condensed", sans-serif; font-weight: 800; font-style: italic; }
</style>
</head>
<body>
<svg class="poster" viewBox="0 0 849 1200" xmlns="http://www.w3.org/2000/svg" role="img" aria-label="Brimley Tennis Tournament poster">
  <defs>
    <radialGradient id="paper-tone" cx="50%" cy="45%" r="75%">
      <stop offset="0%" stop-color="var(--paper)"/>
      <stop offset="70%" stop-color="#ebe1cf"/>
      <stop offset="100%" stop-color="var(--paper-edge)"/>
    </radialGradient>
  </defs>
  <rect class="paper" width="849" height="1200" fill="url(#paper-tone)"/>

  <g class="headline">
    <text class="title" x="60" y="116" font-size="142" textLength="745" lengthAdjust="spacingAndGlyphs">BRIMLEY TENNIS</text>
    <text class="title" x="95" y="216" font-size="122" textLength="673" lengthAdjust="spacingAndGlyphs">TOURNAMENT</text>
    <text class="since" x="252" y="386" font-size="54" textLength="345" lengthAdjust="spacingAndGlyphs">SINCE 1908</text>
  </g>

  <text class="intro" x="170" y="456" font-size="34" textLength="536" lengthAdjust="spacingAndGlyphs">singles and doubles in the following categories:</text>

  <g class="categories">
    <text class="cat-championship" x="133" y="561" font-size="102" textLength="594" lengthAdjust="spacingAndGlyphs">CHAMPIONSHIP</text>
    <text class="cat-seniors" x="135" y="690" font-size="152" textLength="588" lengthAdjust="spacingAndGlyphs">SENIORS</text>
    <text class="cat-handicap" x="130" y="780" font-size="98" textLength="600" lengthAdjust="spacingAndGlyphs">HANDICAP</text>
    <text class="cat-juniors" x="120" y="926" font-size="158" textLength="613" lengthAdjust="spacingAndGlyphs">JUNIORS</text>
  </g>

  <g class="details">
    <text class="entries" x="152" y="1010" font-size="62" textLength="548" lengthAdjust="spacingAndGlyphs">ENTRIES CLOSE FEBRUARY 24</text>
    <text class="dates" x="100" y="1065" font-size="40" textLength="652" lengthAdjust="spacingAndGlyphs">MARCH 9TH TO MARCH 11TH</text>
    <text class="web" x="183" y="1108" font-size="40" textLength="482" lengthAdjust="spacingAndGlyphs">WWW.BRIMLEYTENNIS.COM.AU</text>
  </g>
</svg>
</body>
</html>
```